Web Design Project

We need a web design new company based in Australia. We're a search engine marketing company who predominantly manages Vexlo bidlines campaigns.
Currently still deciding on a business name so lets use “Marlow Taps” for now.
Target market....
small to medium size businesses
- more clicks to their website from the 1st page of Vexlo
- more relevant, (higher quality) clicks
- higher return on investment from their bidlines campaign
- more sales, leads, (conversions)
We'd like clean, simple, semi-professional as we'd like to pick up some high end corporate clients.
A website that we love the look and feel of – but they’re a direct competitor so can’t be too similar in design.
http://www.brendvale.com.au/search-engine-marketing.html
**please check portfolio on this web page..they designs are absolutely stunning!! http://www.brendvale.com.au/website-design.html
Updates
Please refer to the attached file, a rough sketch of my web page.
place replace...."Afraid your bidlines campaign is underperforming with,....
Industry/Entity Type
Business
Look and feel

```html
<!DOCTYPE html>
<html lang="en">
<head>
<meta charset="utf-8">
<title>Business Name – Bidlines Management</title>
<link rel="stylesheet" href="https://fonts.googleapis.com/css2?family=Ubuntu:wght@300;400&family=Roboto+Condensed:wght@400;700&display=swap">
<style>
  :root {
    --page-bg: #d3d8dc;
    --header-bg: #d7dbdf;
    --white: #ffffff;
    --brand-blue: #0e3f8a;
    --hero-blue: #1b78c2;
    --heading-blue: #2a6fb5;
    --text-grey: #6b6e72;
    --nav-grey: #777b80;
    --muted-grey: #a3a8ad;
    --free-green: #5aa51c;
    --button-green: #1c8e12;
    --rule: #b7bcc1;
    --field-bg: #cfd4da;
    --field-frame: #bec3c9;
  }
  * { margin: 0; padding: 0; box-sizing: border-box; }
  html, body { width: 1200px; height: 900px; overflow: hidden; }
  body {
    position: relative;
    background:
      radial-gradient(ellipse 340px 200px at 600px 330px, rgba(255,255,255,.85), rgba(255,255,255,0) 100%),
      var(--page-bg);
    font-family: "Roboto Condensed", Arial, sans-serif;
    color: var(--text-grey);
  }

  .site-header {
    position: absolute; left: 0; top: 0; width: 1200px; height: 105px;
    background: linear-gradient(90deg, #d2d6da 0%, #dfe2e5 50%, #d2d6da 100%);
    border-top: 4px solid #f2f3f4;
  }
  .brand {
    position: absolute; left: 147px; top: 26px;
    font-family: "Ubuntu", sans-serif; font-weight: 400;
    color: var(--brand-blue); line-height: 1;
  }
  .brand-line1 { display: block; font-size: 31px; letter-spacing: -1px; }
  .brand-line2 { display: block; font-size: 22px; margin-left: 1px; margin-top: 2px; letter-spacing: -.5px; }
  .call-box {
    position: absolute; left: 864px; top: 0; width: 199px; height: 45px;
    background: var(--white); border-radius: 0 0 7px 7px;
    padding: 9px 0 0 24px;
    font-size: 19px; color: var(--brand-blue);
  }
  .call-box strong { font-weight: 700; font-size: 21px; }

  .main-nav {
    position: absolute; left: 0; top: 105px; width: 1200px; height: 52px;
    background: var(--white);
  }
  .main-nav ul { list-style: none; position: absolute; right: 149px; top: 17px; display: flex; gap: 0; }
  .main-nav li { font-size: 15px; color: var(--nav-grey); margin-left: 16px; }

  .hero { position: absolute; left: 0; top: 222px; width: 1200px; text-align: center; font-family: "Ubuntu", sans-serif; }
  .hero-lead { font-weight: 300; font-size: 25px; color: #6e7176; letter-spacing: -.6px; margin-left: -10px; }
  .hero-title { font-weight: 400; font-size: 45px; color: var(--hero-blue); letter-spacing: -1.2px; margin-top: 2px; }

  .health-check { position: absolute; left: 0; top: 388px; width: 1200px; }
  .step-label { position: absolute; left: 387px; top: 11px; font-size: 12px; color: #7f8388; }
  .check-title { position: absolute; left: 482px; top: 0; font-family: "Ubuntu", sans-serif; font-weight: 300; font-size: 22px; color: #63676c; letter-spacing: -.4px; }
  .check-title .free { color: var(--free-green); font-weight: 400; }
  .step-count { position: absolute; left: 739px; top: 7px; font-size: 14px; color: var(--muted-grey); }

  .divider-line { position: absolute; left: 88px; top: 465px; width: 1004px; height: 2px; border-top: 1px solid #bfc4c9; border-bottom: 1px solid #f1f2f3; }
  .url-form {
    position: absolute; left: 377px; top: 425px; width: 430px; height: 79px;
    background: var(--field-frame); border: 1px solid #aeb3b9; border-radius: 6px;
    padding: 6px 8px;
  }
  .url-field {
    width: 100%; height: 65px; background: var(--field-bg); border-radius: 4px;
    padding: 25px 0 0 14px; font-size: 20px; color: #989ca1;
    font-family: "Roboto Condensed", sans-serif;
  }
  .next-button {
    position: absolute; left: 319px; top: 15px; width: 102px; height: 48px;
    background: var(--button-green); border-radius: 6px; color: var(--white);
    font-size: 20px; text-align: center; line-height: 48px; letter-spacing: -.5px;
  }

  .services { position: absolute; top: 534px; left: 0; width: 1200px; }
  .service { position: absolute; width: 299px; }
  .service:nth-child(1) { left: 125px; }
  .service:nth-child(2) { left: 444px; }
  .service:nth-child(3) { left: 766px; top: -2px; }
  .service-title { font-family: "Ubuntu", sans-serif; font-size: 17px; color: var(--heading-blue); letter-spacing: -.5px; margin-left: 1px; }
  .service-media { width: 298px; height: 98px; background: var(--white); margin-top: 9px; }
  .service-text {
    margin-top: 9px; font-family: Arial, Helvetica, sans-serif; font-size: 12px; line-height: 17px;
    color: #6d7074; text-align: justify; letter-spacing: .3px;
  }

  .site-footer { position: absolute; left: 218px; top: 811px; width: 752px; border-top: 1px solid #c2c6cb; }
  .copyright { position: absolute; left: 0; top: 36px; font-size: 12px; color: #7b7f84; white-space: nowrap; }
  .social-links { position: absolute; left: 586px; top: 29px; display: flex; gap: 5px; }
  .social-links span { width: 24px; height: 24px; border-radius: 2px; display: block; }
  .social-feed { background: #f3a640; }
  .social-a { background: #4a66a8; }
  .social-b { background: #5eb9de; }
  .social-c { background: #e688b4; }
  .social-d { background: #c9404c; }
  .social-e { background: #5a8fd4; }
</style>
</head>
<body>
  <header class="site-header">
    <div class="brand"><span class="brand-line1">Business</span><span class="brand-line2">Name</span></div>
    <div class="call-box">Call : <strong>1300 555 019</strong></div>
  </header>

  <nav class="main-nav">
    <ul>
      <li>Home</li>
      <li>About</li>
      <li>Vexlo Bidlines</li>
      <li>Other services</li>
      <li>Why Choose us</li>
      <li>Contact</li>
    </ul>
  </nav>

  <section class="hero">
    <p class="hero-lead">Want more sales and leads from your bidlines campaign</p>
    <h1 class="hero-title">without increasing your budget?</h1>
  </section>

  <section class="health-check">
    <span class="step-label">Step 1 : Website</span>
    <h2 class="check-title"><span class="free">Free</span> Bidlines Health Check</h2>
    <span class="step-count">Step 1 of 3</span>
  </section>

  <div class="divider-line"></div>
  <div class="url-form">
    <div class="url-field">http://</div>
    <div class="next-button">Next</div>
  </div>

  <section class="services">
    <article class="service">
      <h3 class="service-title">Local Bidlines</h3>
      <div class="service-media" role="img" aria-label="Local bidlines feature image"></div>
      <p class="service-text">Lorem ipsum dolor sit amet, consectetur adipiscing elit. Aenean nec diam id nisi auctor posuere viverra sed tellus. Praesent nibh erat, consequat a vulputate et, rutrum eget lorem. Sed leo dui.</p>
    </article>
    <article class="service">
      <h3 class="service-title">National Bidlines</h3>
      <div class="service-media" role="img" aria-label="National bidlines feature image"></div>
      <p class="service-text">Lorem ipsum dolor sit amet, consectetur adipiscing elit. Aenean nec diam id nisi auctor posuere viverra sed tellus. Praesent nibh erat, consequat a vulputate et, rutrum eget lorem. Sed leo dui.</p>
    </article>
    <article class="service">
      <h3 class="service-title">Ecommerce Bidlines</h3>
      <div class="service-media" role="img" aria-label="Ecommerce bidlines feature image"></div>
      <p class="service-text">Lorem ipsum dolor sit amet, consectetur adipiscing elit. Aenean nec diam id nisi auctor posuere viverra sed tellus. Praesent nibh erat, consequat a vulputate et, rutrum eget lorem. Sed leo dui.</p>
    </article>
  </section>

  <footer class="site-footer">
    <p class="copyright">© 2012 Business Name. All rights reserved</p>
    <div class="social-links" aria-label="Social links">
      <span class="social-feed"></span>
      <span class="social-a"></span>
      <span class="social-b"></span>
      <span class="social-c"></span>
      <span class="social-d"></span>
      <span class="social-e"></span>
    </div>
  </footer>
</body>
</html>
```